Author book launch promotion design for social media

We are organising an authors book launch event and require an author promotion design that will be used on social media (Chatterbook, netted) promotion.

The design must have the author's photo, image of their book, the event logo, details of the event plus website address (penfairhall.com.au).

Details of the event can be found at penfairhall.com.au.

the design has to be attractive and inviting and colours in accordance with the brand colours.

You can choose 1 one of the book images attached
Author name: Dr Tarek Bismil
Event Details
LAUNCH YOUR BOOK IN STYLE

Quillmark Reading Fair and Showcase 2022
7 - 8 October 2022
Melbourne Larkvale Centre
14 Corrigal St, Southbank Melbourne

For registration and ticketing visit:
penfairhall.com.au

I have attached also a sample promo. Please be creative.

```html
<!DOCTYPE html>
<html lang="en">
<head>
<meta charset="utf-8">
<title>Launch Your Book in Style – Quillmark Reading Fair and Showcase 2022</title>
<link rel="stylesheet" href="https://fonts.googleapis.com/css2?family=Montserrat:wght@500;600;700;800&family=Great+Vibes&display=swap">
<style>
  :root {
    --stage: #e4e4e4;
    --cream: #fef2df;
    --cream-deep: #fde6c4;
    --white: #ffffff;
    --teal: #137c8b;
    --rose: #d24a5e;
    --navy: #0f3553;
    --gold: #e8b04a;
    --gold-dark: #c49a2c;
    --arch: #ecb04b;
    --ring: #f2efe9;
    --disc: #12395a;
  }
  * { margin: 0; padding: 0; box-sizing: border-box; }
  html, body {
    width: 1200px; height: 748px; overflow: hidden;
    background: var(--stage);
    font-family: "Montserrat", Arial, sans-serif;
  }
  .promo {
    position: absolute; left: 0; top: 60px;
    width: 1200px; height: 628px; overflow: hidden;
    background:
      linear-gradient(200deg, var(--cream-deep) 0%, var(--cream) 45%, var(--white) 100%);
  }
  .headline-tag {
    position: absolute; left: 43px;
    height: 68px; padding: 0 18px;
    color: var(--white); font-weight: 700; font-size: 53px;
    line-height: 68px; letter-spacing: 0.3px; white-space: nowrap;
  }
  .headline-tag--launch { top: 79px; width: 275px; background: var(--teal); }
  .headline-tag--book { top: 158px; width: 460px; background: var(--rose); }
  .headline-script {
    position: absolute; left: 54px; top: 240px;
    font-family: "Great Vibes", cursive;
    font-size: 138px; line-height: 1; color: var(--gold);
    letter-spacing: 2px; white-space: nowrap;
  }
  .event-title {
    position: absolute; left: 364px; top: 258px;
    font-size: 32px; line-height: 44px; font-weight: 700; color: var(--navy);
    white-space: nowrap;
  }
  .event-title .accent { color: var(--teal); }
  .event-title .light { font-weight: 500; color: var(--teal); }
  .date-band {
    position: absolute; left: 0; top: 409px; width: 392px; height: 87px;
  }
  .date-band svg { position: absolute; inset: 0; }
  .date-band__text { position: absolute; left: 47px; top: 10px; color: var(--white); white-space: nowrap; }
  .date-band__date { font-size: 23px; font-weight: 700; line-height: 26px; }
  .date-band__venue { font-size: 15px; font-weight: 500; line-height: 22px; }
  .event-mark {
    position: absolute; left: 433px; top: 415px; width: 235px;
    text-align: center; font-size: 37px; font-weight: 800;
    color: var(--gold-dark); letter-spacing: 1px;
  }
  .registration {
    position: absolute; left: 47px; top: 528px;
    border-left: 4px solid var(--gold); padding-left: 14px;
  }
  .registration__lead { font-size: 15px; font-weight: 700; color: var(--navy); line-height: 19px; }
  .registration__url { font-size: 34px; font-weight: 700; color: var(--teal); line-height: 40px; }
  .author-name {
    position: absolute; left: 776px; top: 66px;
    font-size: 36px; line-height: 40px; font-weight: 700; color: var(--navy); white-space: nowrap;
  }
  .author-visual { position: absolute; left: 700px; top: 110px; width: 460px; height: 518px; }
  .author-visual svg { position: absolute; inset: 0; }
</style>
</head>
<body>
  <main class="promo">
    <div class="headline-tag headline-tag--launch">LAUNCH</div>
    <div class="headline-tag headline-tag--book">YOUR BOOK IN</div>
    <div class="headline-script">Style</div>

    <h1 class="event-title">
      Quillmark Reading Fair<br>
      <span class="light">and</span> <span class="accent">Showcase 2022</span>
    </h1>

    <div class="date-band">
      <svg width="392" height="87" viewBox="0 0 392 87" aria-hidden="true">
        <polygon points="0,0 345,0 392,87 0,87" fill="var(--rose)"/>
      </svg>
      <div class="date-band__text">
        <div class="date-band__date">7 - 8 October 2022</div>
        <div class="date-band__venue">Melbourne Larkvale Centre</div>
        <div class="date-band__venue">14 Corrigal St, Southbank Melbourne</div>
      </div>
    </div>

    <div class="event-mark">QUILLMARK</div>

    <div class="registration">
      <div class="registration__lead">For registration and ticketing visit:</div>
      <div class="registration__url">penfairhall.com.au</div>
    </div>

    <div class="author-name">Dr Tarek Bismil</div>

    <div class="author-visual">
      <svg width="460" height="518" viewBox="0 0 460 518">
        <defs>
          <linearGradient id="portraitTone" x1="0" y1="0" x2="0" y2="1">
            <stop offset="0" stop-color="#5a4638"/>
            <stop offset="0.35" stop-color="#b98e74"/>
            <stop offset="0.5" stop-color="#3a3c40"/>
            <stop offset="1" stop-color="#26282c"/>
          </linearGradient>
          <linearGradient id="bookTone" x1="0" y1="0" x2="0" y2="1">
            <stop offset="0" stop-color="#f1f1f1"/>
            <stop offset="1" stop-color="#9aa0a8"/>
          </linearGradient>
        </defs>
        <path d="M78 64 H226 A200 200 0 0 1 426 264 V475 H78 Z" fill="var(--arch)"/>
        <rect role="img" aria-label="Portrait photo of author Dr Tarek Bismil in a dark suit" x="126" y="10" width="284" height="465" rx="90" fill="url(#portraitTone)"/>
        <circle cx="126" cy="387" r="117" fill="var(--ring)"/>
        <circle cx="126" cy="387" r="108" fill="var(--disc)"/>
        <rect role="img" aria-label="Photo of the author's book standing on a copy lying flat" x="39" y="249" width="198" height="206" rx="3" fill="url(#bookTone)"/>
      </svg>
    </div>
  </main>
</body>
</html>
```